Business card design for a teacher - double sided, sleek design.

My name is Dalia and I am an online Arabic language teacher. I am looking for a beautiful business card design for my online teaching business.

The cards will be printed in 85mm x 55mm size.
The card can be either portrait or landscape.

The design should contain my logo on one side and information on the other.

The design needs to be clean and modern. Use of subtle Arabic geometric patterns would be nice. Icons for the social media information on the card should also match the design theme.

My logo font is Consolas, which is a Monospace font.

Business card design should be delivered with editable PSD or EPS files in the handover.

Thanks

Dalia

----

Information on the back:

URL: www.lughapathway.net [this should stand out more than other details]
Email: info@lughapathway.net
Instagram: @lughapathway
Facebook: linkora.net/lughapathway
Skype: lughapathway

My brand colours are shown in the logo attached. These are:
- Teal green - 4DC9C1
- Mango yellow - FFD600

Target Market(s)

- Young professionals
- Expatriates
- Women and Men

Industry/Entity Type

Education

Contact Information for Business Card

Information on the back:

Skype: lughapathway

- Teal green - 4DC9C1
- Mango yellow - FFD600

Font styles to use
Other font styles liked:
• Any font complimentary to my logo font which is a Monospace font called Consolas.

Colors

Designer to choose colors to be used in the design.

Requirements
Must have
• - Aesthetically pleasing look
• - Complimentary design with existing logo
Nice to have
• Arabic geometrical patterns

```html
<!DOCTYPE html>
<html lang="en">
<head>
<meta charset="utf-8">
<title>Lugha Pathway – Business Cards</title>
<link rel="stylesheet" href="https://fonts.googleapis.com/css2?family=Source+Code+Pro:wght@400;500&family=Open+Sans:wght@400&display=swap">
<style>
  :root {
    --teal: #4dc9c1;
    --teal-deep: #45bdb5;
    --teal-soft: #5fd0c8;
    --mango: #ffd600;
    --ink: #2b2b2b;
    --slate: #555a5a;
    --white: #ffffff;
    --stage: #d9dbdb;
  }
  * { box-sizing: border-box; margin: 0; padding: 0; }
  html, body { width: 1200px; height: 900px; overflow: hidden; }
  body {
    background: var(--stage);
    display: flex;
    align-items: center;
    justify-content: center;
    gap: 44px;
  }
  .card {
    position: relative;
    width: 540px;
    height: 349px;
    border-radius: 26px;
    overflow: hidden;
    box-shadow: 0 10px 26px rgba(0,0,0,.18);
  }

  /* Shared wordmark */
  .brand {
    display: flex;
    align-items: center;
    gap: 14px;
  }
  .brand-dot {
    flex: none;
    width: 18px;
    height: 18px;
    border-radius: 50%;
    background: var(--mango);
  }
  .brand-name {
    font-family: "Source Code Pro", monospace;
    font-weight: 500;
    font-size: 34px;
    letter-spacing: 1px;
    line-height: 1;
    white-space: nowrap;
  }

  /* Logo side */
  .card--front { background: var(--teal); }
  .pattern-field {
    position: absolute;
    inset: 0;
    background: radial-gradient(ellipse at 50% 50%, var(--teal-soft) 0%, var(--teal) 55%, var(--teal-deep) 100%);
  }
  .front-content {
    position: absolute;
    inset: 0;
    display: flex;
    flex-direction: column;
    align-items: center;
    justify-content: center;
    gap: 30px;
  }
  .card--front .brand-name { color: var(--white); }
  .front-url {
    font-family: "Source Code Pro", monospace;
    font-size: 17px;
    letter-spacing: 3px;
    color: var(--white);
  }

  /* Information side */
  .card--back { background: var(--white); }
  .back-brand {
    position: absolute;
    left: 38px;
    top: 46px;
  }
  .back-brand .brand-dot { width: 14px; height: 14px; }
  .back-brand .brand-name { font-size: 26px; color: var(--slate); }
  .contact {
    position: absolute;
    left: 238px;
    top: 124px;
    width: 280px;
  }
  .contact-rule {
    width: 64px;
    height: 2px;
    background: var(--teal);
  }
  .contact-rule--top { margin-left: 52px; margin-bottom: 16px; }
  .contact-rule--bottom { margin-top: 16px; }
  .contact-list { list-style: none; }
  .contact-item {
    display: flex;
    align-items: center;
    gap: 9px;
    font-family: "Open Sans", sans-serif;
    font-size: 15px;
    color: var(--ink);
    line-height: 1.75;
    white-space: nowrap;
  }
  .contact-dot {
    flex: none;
    width: 11px;
    height: 11px;
    border-radius: 50%;
    background: var(--teal);
  }
  .url-band {
    position: absolute;
    left: 0;
    right: 0;
    bottom: 0;
    height: 66px;
    background: var(--teal);
    display: flex;
    align-items: center;
    padding-left: 42px;
  }
  .url-band-text {
    font-family: "Source Code Pro", monospace;
    font-size: 19px;
    letter-spacing: 3px;
    color: var(--mango);
  }
</style>
</head>
<body>

  <section class="card card--front" aria-label="Card front">
    <div class="pattern-field" role="img" aria-label="Subtle Arabic geometric star pattern in teal tones"></div>
    <div class="front-content">
      <div class="brand">
        <span class="brand-dot"></span>
        <span class="brand-name">Lugha Pathway</span>
      </div>
      <p class="front-url">www.lughapathway.net</p>
    </div>
  </section>

  <section class="card card--back" aria-label="Card back">
    <div class="brand back-brand">
      <span class="brand-dot"></span>
      <span class="brand-name">Lugha Pathway</span>
    </div>
    <div class="contact">
      <div class="contact-rule contact-rule--top"></div>
      <ul class="contact-list">
        <li class="contact-item"><span class="contact-dot"></span>@lughapathway</li>
        <li class="contact-item"><span class="contact-dot"></span>linkora.net/lughapathway</li>
        <li class="contact-item"><span class="contact-dot"></span>lughapathway</li>
      </ul>
      <div class="contact-rule contact-rule--bottom"></div>
    </div>
    <div class="url-band">
      <p class="url-band-text">www.lughapathway.net</p>
    </div>
  </section>

</body>
</html>
```